Business Card Tevan Law llc examples and ideas are attached.

in addition to the logo we need a desription what we do: "Reprsenting students with disabilites obtain services to progress in the public school system."

If you can squeeze it on the fron at the bottom great if not put it on the back

```html
<!DOCTYPE html>
<html lang="en">
<head>
<meta charset="utf-8">
<title>Tevan Law LLC – Business Card</title>
<link href="https://fonts.googleapis.com/css2?family=Roboto:wght@400;500;700&display=swap" rel="stylesheet">
<style>
  :root {
    --page-bg: #e6e7ea;
    --card-bg: #ffffff;
    --navy: #134a7c;
    --text-grey: #5f6368;
    --rule-grey: #8a8d91;
    --gold-dark: #c9a96b;
    --gold-light: #f4df8c;
  }
  * { margin: 0; padding: 0; box-sizing: border-box; }
  html, body {
    width: 1200px; height: 1000px; overflow: hidden;
    background: var(--page-bg);
    font-family: "Roboto", Arial, sans-serif;
  }
  .business-card {
    position: absolute; left: 297px; top: 314px;
    width: 640px; height: 364px;
    background: var(--card-bg);
    overflow: hidden;
  }
  .brand-square {
    position: absolute; left: 132px; top: 39px;
    width: 53px; height: 53px;
    border: 2px solid var(--navy);
  }
  .brand-name {
    position: absolute; left: 51px; top: 101px;
    font-size: 27px; font-weight: 500; color: var(--navy);
    letter-spacing: 1.1px; white-space: nowrap;
  }
  .practice-mission {
    position: absolute; right: 50px; top: 150px;
    width: 250px; text-align: right;
    font-size: 12.5px; line-height: 18px; color: var(--text-grey);
  }
  .person-name {
    position: absolute; left: 51px; top: 214px;
    font-size: 19px; font-weight: 700; color: var(--navy);
    letter-spacing: 0.2px;
  }
  .person-title {
    position: absolute; left: 51px; top: 239px;
    font-size: 14.5px; color: var(--text-grey);
  }
  .title-rule {
    position: absolute; left: 162px; top: 248px;
    width: 428px; height: 1.5px; background: var(--rule-grey);
  }
  .contact-list {
    position: absolute; left: 51px; top: 284px;
    list-style: none; font-size: 14.5px; color: var(--text-grey);
  }
  .contact-list li { display: flex; align-items: center; height: 21px; }
  .contact-list svg { width: 13px; height: 13px; margin-right: 7px; fill: var(--navy); }
  .office-address {
    position: absolute; right: 50px; top: 261px;
    font-style: normal; text-align: right;
    font-size: 14.5px; line-height: 20px; color: var(--text-grey);
  }
  .office-address sup { font-size: 9px; }
  .footer-bands { position: absolute; left: 0; bottom: 0; width: 640px; height: 26px; }
  .practice-area {
    position: absolute; left: 393px; bottom: 5px; width: 240px;
    text-align: center; font-size: 14.5px; color: #fff;
  }
</style>
</head>
<body>
  <div class="business-card">
    <div class="brand-square"></div>
    <div class="brand-name">TEVAN LAW LLC</div>

    <p class="practice-mission">Representing students with disabilities obtain services to progress in the public school system.</p>

    <div class="person-name">DANIEL R TEVAN</div>
    <div class="person-title">Attorney at Law</div>
    <div class="title-rule"></div>

    <ul class="contact-list">
      <li>
        <svg viewBox="0 0 24 24"><path d="M6.6 10.8a15 15 0 0 0 6.6 6.6l2.2-2.2c.3-.3.7-.4 1-.2 1.1.4 2.3.6 3.6.6.6 0 1 .4 1 1V20c0 .6-.4 1-1 1A17 17 0 0 1 3 4c0-.6.4-1 1-1h3.5c.6 0 1 .4 1 1 0 1.3.2 2.5.6 3.6.1.3 0 .7-.2 1z"/></svg>
        813 555 0142
      </li>
      <li>
        <svg viewBox="0 0 24 24"><path d="M2 5h20v14H2z" fill="var(--navy)"/><path d="M3 6l9 7 9-7" fill="none" stroke="#fff" stroke-width="1.6"/></svg>
        dan.tevanlaw@mail.com
      </li>
    </ul>

    <address class="office-address">
      1450 NE 18<sup>th</sup> Ave<br>
      Fort Lauderdale FL33305<br>
      By appointment only
    </address>

    <svg class="footer-bands" viewBox="0 0 640 26" preserveAspectRatio="none">
      <defs>
        <linearGradient id="goldBand" x1="0" x2="1" y1="0" y2="0">
          <stop offset="0" stop-color="var(--gold-dark)"/>
          <stop offset="0.7" stop-color="#ddc27f"/>
          <stop offset="1" stop-color="var(--gold-light)"/>
        </linearGradient>
      </defs>
      <polygon points="0,11 396,11 383,26 0,26" fill="url(#goldBand)"/>
      <polygon points="414,0 640,0 640,26 390,26" fill="var(--navy)"/>
    </svg>
    <div class="practice-area">Special Education Law</div>
  </div>
</body>
</html>
```